Redesign Craft Brewing Recipe Website

Originally built with Bootstrap just to get the site going, I am seeking a complete redesign of the sites home page and recipe page. I am an experienced web developer with no graphic background, initially just looking for psd mocks.

I prefer styles that are clean and modern, and would prefer anything that is fun, engaging, and has an organic feel to it. I currently have a cartoon rabbit as a logo, but it needs some modification/tweaking, so any help in that area would be great as well.

Current site:
http://kettlewren.plumhostsite.net/

Current launch page/logo:
http://www.kettlewren.com/

I like the overall layout of the elements currently, but the design sucks.

The launch page is at the following URL

Reason: Still looking for a more modern design. Designs received so far are too similar to the original.

My site is content based and does not contain images or products. Your design should not consist of large images.

Reason: The website has very little images, so the designs need to be more text and content based. The header needs to be very small and should not contain an ad rotater.

Target Market(s)

Home brewers, Craft brewers, Microbreweries, Brewpubs

Requirements
Must have
• Web 2.0 Look and Feel, Fun, Hip, Focus on content
Should not have
• A large photo as a header

```html
<!DOCTYPE html>
<html lang="en">
<head>
<meta charset="utf-8">
<title>KettleWren — craft beer recipes</title>
<link href="https://fonts.googleapis.com/css2?family=Raleway:wght@300;400;500;600;700;800&display=swap" rel="stylesheet">
<style>
:root{
  --bar:#1b1b20;
  --bar-light:#2c2c33;
  --gold:#c8870e;
  --brown:#6e3a0c;
  --red:#a51c1c;
  --grey:#8a8a8a;
  --text:#555;
  --ink:#222;
  --link:#2a84b8;
  --ad:#e6e6e6;
}
*{box-sizing:border-box;margin:0;padding:0}
html,body{width:813px;height:1200px;overflow:hidden;background:#fff}
body{font-family:"Raleway",sans-serif;color:var(--text);font-variant-numeric:lining-nums}
.canvas{position:relative;width:813px;height:1200px;overflow:hidden}
.page{position:absolute;left:0;top:0;width:1000px;height:1476px;transform:scale(.813);transform-origin:0 0}
.abs{position:absolute}

.topbar{left:0;top:0;width:1000px;height:50px;background:linear-gradient(var(--bar-light),var(--bar))}
.avatar-sm{left:40px;top:12px;width:26px;height:26px;border-radius:3px;background:linear-gradient(#cfb8a4,#5c4a3e);border:1px solid #888}
.welcome{left:78px;top:17px;color:#fff;font-weight:700;font-size:13px}
.tool{top:15px;color:#aaa;font-size:13px;display:flex;align-items:center;gap:6px}
.tool svg{fill:#ddd}
.logout{left:764px;top:17px;color:#3aa8e0;font-size:13px}
.join{left:828px;top:8px;width:110px;height:33px;background:linear-gradient(#ffd14a,#f6a800);border:1px solid #e09a00;color:#2a1b00;font-weight:700;letter-spacing:1.5px;font-size:13px;display:flex;align-items:center;justify-content:center}
.account-menu{left:34px;top:47px;width:140px;height:70px;background:#fff;box-shadow:0 2px 6px rgba(0,0,0,.25);padding:8px 6px}
.account-menu li{list-style:none;font-size:9px;font-weight:800;color:#222;height:20px}
.account-menu::before{content:"";position:absolute;left:10px;top:-6px;border:6px solid transparent;border-top:0;border-bottom-color:#fff}

.brand{left:0;top:80px;width:1000px;text-align:center;font-size:34px;font-weight:600;color:var(--gold);letter-spacing:-.5px}
.tagline{left:0;top:140px;width:1010px;text-align:center;font-size:16px;letter-spacing:2px;color:#7a4a10}

.mainnav{left:0;top:198px;width:1000px;height:48px;background:var(--gold)}
.mainnav a{position:absolute;top:13px;color:#fff;font-weight:700;font-size:17px;text-decoration:none;text-transform:uppercase}
.search{left:673px;top:8px;width:266px;height:31px;background:#fff;border-radius:3px;font-style:italic;color:#999;font-size:12px;padding:8px 12px}
.search svg{position:absolute;right:8px;top:5px}

.styles{left:34px;top:270px;width:891px;font-size:14px;font-weight:500;color:var(--grey);text-transform:uppercase}
.styles span{position:absolute;white-space:nowrap}
.styles .active{color:var(--ink);border-left:3px solid var(--ink);padding-left:6px}
.divider{left:34px;top:299px;width:891px;height:1px;background:#ddd}
.ads{left:44px;top:361px;width:877px;height:86px;background:var(--ad);display:flex;align-items:center;justify-content:center;font-size:16px;color:#555}

.feat-title{font-size:21px;font-weight:400;color:var(--brown);text-transform:uppercase;display:flex;align-items:center;gap:6px}
.date{font-size:11px;color:#333}
.thumb{width:90px;height:90px;border-radius:50%;border:3px solid #efe3c3}
.rtitle{font-size:15px;font-weight:600;color:var(--red);display:flex;align-items:center;gap:14px;white-space:nowrap}
.tag{background:#e19a2a;color:#fff;font-size:10px;padding:2px 9px;border-radius:2px;font-weight:500}
.lorem{font-size:12px;line-height:15.5px;color:#666;text-align:justify}
.by{font-size:13px;color:#555}
.by b{font-weight:500;color:#333}

.col-title{font-size:21px;color:var(--brown);text-transform:uppercase;font-weight:400}
.rank{width:26px;height:26px;border-radius:50%;border:2px solid #444;font-size:13px;font-weight:700;color:#333;display:flex;align-items:center;justify-content:center}
.pop-name{font-size:15px;font-weight:500;color:var(--red);letter-spacing:.3px}
.pop-by{font-size:13px;color:#555;letter-spacing:.3px}
.user-pic{width:46px;height:46px;border-radius:50%;border:3px solid #e2e2e2;background:radial-gradient(circle at 50% 40%,#b9a58f,#3a3430)}
.user-name{font-size:15px;color:#5a2c08;display:flex;align-items:center;gap:5px}
.friend{font-size:11px;font-style:italic;color:var(--link)}
.flag{display:inline-block;width:16px;height:11px}
.thread{font-size:12px;font-weight:700;color:#9c0e0e;white-space:nowrap}
.view{font-size:11px;font-style:italic;color:var(--link)}
</style>
</head>
<body>
<div class="canvas">
<div class="page">

  <header class="abs topbar">
    <div class="abs avatar-sm" role="img" aria-label="Member profile photo"></div>
    <div class="abs welcome">Welcome, Junior</div>
    <div class="abs tool" style="left:205px"><svg width="18" height="16" viewBox="0 0 18 16"><path d="M1 1h16v10H7l-4 4v-4H1z"/></svg>No new messages</div>
    <div class="abs tool" style="left:354px"><svg width="20" height="17" viewBox="0 0 20 17"><path d="M10 16 2 8a4.5 4.5 0 0 1 8-5 4.5 4.5 0 0 1 8 5z"/></svg>Recipes liked</div>
    <div class="abs tool" style="left:482px"><svg width="22" height="20" viewBox="0 0 22 20" fill="none" stroke="#ddd" stroke-width="2"><path d="M14 2H2v16h16V8"/><path d="M8 12l1-4 9-7 2 2-8 8z" fill="#ddd"/></svg>&nbsp;Edit profile</div>
    <div class="abs tool" style="left:597px"><svg width="22" height="20" viewBox="0 0 22 20"><circle cx="4" cy="10" r="3.5"/><circle cx="18" cy="3.5" r="3.5"/><circle cx="18" cy="16.5" r="3.5"/><path d="M4 10 18 3.5M4 10l14 6.5" stroke="#ddd" stroke-width="2"/></svg>&nbsp;Share</div>
    <div class="abs logout">Logout</div>
    <div class="abs join">JOIN US</div>
  </header>
  <ul class="abs account-menu">
    <li>MY ACCOUNT</li><li>SET ANOTHER PICTURE</li><li>VIEW MY PROFILE</li>
  </ul>

  <div class="abs brand">KETTLEWREN</div>
  <div class="abs tagline">easiest way to create and share craft beer recipes</div>

  <nav class="abs mainnav">
    <a style="left:34px">Featured recipes</a>
    <a style="left:253px">Our jury</a>
    <a style="left:394px">Submit your recipe</a>
    <div class="abs search">Find recipe....
      <svg width="24" height="24" viewBox="0 0 24 24"><circle cx="9" cy="9" r="6.5" fill="none" stroke="#ccc" stroke-width="3"/><path d="M14 14l7 7" stroke="#ccc" stroke-width="4" stroke-linecap="round"/></svg>
    </div>
  </nav>

  <div class="abs styles">
    <span class="active" style="left:0;top:2px">American Barleywine</span>
    <span style="left:202px;top:2px">Blonde Ale</span>
    <span style="left:319px;top:2px">Bohemian Pilsner</span>
    <span style="left:485px;top:2px">American Brown Ale</span>
    <span style="left:670px;top:2px">Common Cider</span>
    <span style="left:802px;top:2px">English IPA</span>
    <span style="left:9px;top:42px">Cream Ale</span>
    <span style="left:114px;top:42px">Belgian Dubbel</span>
    <span style="left:255px;top:42px">American Stout</span>
    <span style="left:408px;top:42px">Dunkelweizen</span>
    <span style="left:542px;top:42px">Eisbock</span>
    <span style="left:625px;top:42px">Dark American Lager</span>
    <span style="left:806px;top:42px">Braggot</span>
  </div>
  <div class="abs divider"></div>

  <div class="abs ads">ads</div>

  <h2 class="abs feat-title" style="left:32px;top:493px">Recipe of the day
    <svg width="20" height="26" viewBox="0 0 20 26"><path d="M4 14l-3 10 5-2 3 4 1-10zM16 14l3 10-5-2-3 4-1-10z" fill="#d9a24a"/><circle cx="10" cy="9" r="8" fill="#d9a24a"/></svg></h2>
  <div class="abs date" style="left:34px;top:520px">(23/03/2013)</div>
  <div class="abs thumb" style="left:33px;top:556px;background:radial-gradient(circle at 50% 45%,#f6a640,#a85a12 70%,#5b3a1c)" role="img" aria-label="Pint of amber ale"></div>
  <div class="abs rtitle" style="left:139px;top:548px">Venom Belgian Specialty Ale <span class="tag">PartialMash</span></div>
  <p class="abs lorem" style="left:139px;top:582px;width:310px">Lorem ipsum dolor sit amet, consectetur adipisicing elit, ut labore et dolore magna aliqua.</p>
  <div class="abs by" style="left:139px;top:630px">created by <b>Dale Ostrander</b></div>

  <h2 class="abs feat-title" style="left:516px;top:493px">Recipe of the week
    <svg width="26" height="24" viewBox="0 0 26 24"><path d="M6 2h14v6a7 7 0 0 1-14 0z" fill="#d9a24a"/><path d="M6 4H2a5 5 0 0 0 5 7M20 4h4a5 5 0 0 1-5 7" fill="none" stroke="#d9a24a" stroke-width="2"/><rect x="11" y="14" width="4" height="5" fill="#d9a24a"/><rect x="8" y="19" width="10" height="3" fill="#d9a24a"/></svg></h2>
  <div class="abs date" style="left:514px;top:520px">(16/09/2013 - 25/09/2013)</div>
  <div class="abs thumb" style="left:506px;top:556px;background:radial-gradient(circle at 50% 55%,#f2a21c,#f7d47a 55%,#fdfaf0 75%)" role="img" aria-label="Glass of golden lager with foam"></div>
  <div class="abs rtitle" style="left:612px;top:548px">Venom Belgian Specialty Ale <span class="tag">PartialMash</span></div>
  <p class="abs lorem" style="left:612px;top:582px;width:309px">Lorem ipsum dolor sit amet, consectetur adipisicing elit, sed do eiusmod tempor incididunt ut labore et dolore magna aliqua.</p>
  <div class="abs by" style="left:612px;top:646px">created by <b>Dale Ostrander</b></div>

  <h2 class="abs col-title" style="left:32px;top:750px">Popular recipes</h2>
  <div class="abs rank" style="left:34px;top:797px">1</div>
  <div class="abs pop-name" style="left:71px;top:798px">Venom Mild</div><div class="abs pop-by" style="left:71px;top:816px">by Jules</div>
  <div class="abs rank" style="left:34px;top:849px">2</div>
  <div class="abs pop-name" style="left:71px;top:848px">Oak Bastard Dry Mead</div><div class="abs pop-by" style="left:71px;top:866px">by Luckiest032</div>
  <div class="abs rank" style="left:34px;top:899px">3</div>
  <div class="abs pop-name" style="left:71px;top:898px">Honeysucker Belgian Tripel</div><div class="abs pop-by" style="left:71px;top:916px">by Jules</div>
  <div class="abs rank" style="left:34px;top:953px">4</div>
  <div class="abs pop-name" style="left:71px;top:951px">Moon Man Blonde Ale</div><div class="abs pop-by" style="left:71px;top:969px">by Jules</div>

  <h2 class="abs col-title" style="left:382px;top:748px">Popular users</h2>
  <div class="abs user-pic" style="left:381px;top:799px" role="img" aria-label="User profile photo"></div>
  <div class="abs user-name" style="left:435px;top:804px">Dale Ostrander <svg class="flag" viewBox="0 0 16 11"><rect width="16" height="4" fill="#222"/><rect y="4" width="16" height="3.5" fill="#d00"/><rect y="7.5" width="16" height="3.5" fill="#fc0"/></svg></div>
  <div class="abs friend" style="left:435px;top:824px">add as a friend</div>
  <div class="abs user-pic" style="left:381px;top:859px" role="img" aria-label="User profile photo"></div>
  <div class="abs user-name" style="left:435px;top:866px">Luckiest032 <svg class="flag" viewBox="0 0 16 11"><rect width="16" height="11" fill="#fff"/><rect width="4" height="11" fill="#d52b1e"/><rect x="12" width="4" height="11" fill="#d52b1e"/><circle cx="8" cy="5.5" r="2" fill="#d52b1e"/></svg></div>
  <div class="abs friend" style="left:435px;top:887px">add as a friend</div>
  <div class="abs user-pic" style="left:381px;top:918px" role="img" aria-label="User profile photo"></div>
  <div class="abs user-name" style="left:435px;top:922px">Beerlover12 <svg class="flag" viewBox="0 0 16 11"><rect width="16" height="11" fill="#fff"/><path d="M0 0h16v1.5H0zM0 3h16v1.5H0zM0 6h16v1.5H0zM0 9.5h16V11H0z" fill="#c22"/><rect width="7" height="6" fill="#3b3b8c"/></svg></div>
  <div class="abs friend" style="left:435px;top:943px">add as a friend</div>

  <h2 class="abs col-title" style="left:662px;top:748px">Discussion</h2>
  <div class="abs thread" style="left:665px;top:803px">sed do eiusmod tempor incididunt?</div><div class="abs view" style="left:665px;top:819px">view thread</div>
  <div class="abs thread" style="left:665px;top:843px">sed do eiusmod tempor incididunt?</div><div class="abs view" style="left:665px;top:859px">view thread</div>
  <div class="abs thread" style="left:665px;top:883px">sed do eiusmod tempor incididunt?</div><div class="abs view" style="left:665px;top:898px">view thread</div>
  <div class="abs thread" style="left:665px;top:923px">sed do eiusmod tempor incididunt?</div><div class="abs view" style="left:665px;top:938px">view thread</div>
  <div class="abs thread" style="left:665px;top:963px">sed do eiusmod tempor incididunt?</div><div class="abs view" style="left:665px;top:978px">view thread</div>

</div>
</div>
</body>
</html>
```